Wine Label for White and Red Wine from California

We need a wine label for 2 whites and 2 red wines. (Merlot, Cabernet Sauvignon, Chardonnay, Pinot Grigio) Can be the same label or can have something to differentiate among them such as a color change. This is a label for an already existing wine on the US market but needs to be completely re-done. We want something way sharper, eye catching. Don't use the original label please as your starting point-- I don't think we want to see it anymore. But the structure of it is ok and the fonts are ok. (The tree is what is so awful about)

Target Market(s)

US market, always good to think of millennials, but still appeal to all ages. Men and women.

Colors

Designer to choose colors to be used in the design.

Requirements
Must have
• Should be eye catching, grabs attention, looks expensive, sells for a value price. Should feature the brand name and varietal and vintage:
• Dorvane Vineyards / Cabernet Sauvignon / 2014
• Bottle type is the 'Bordeaux Style' bottle. The white wine is a green bottle, the red wine uses a dark brown bottle. Be sure the labels look good on these bottles.
• What this bottle looks like is shown below.
• The label we are replacing is shown in the briefs.
Nice to have
• We feel successful labels have a lot of white background, stay away from dark labels-- they scratch too much when handled.
• Attached is a label we like, please look at the Cadenza label image below. But at the same time, we are flexible to your creativity. But nothing too crazy please.
Should not have
• Should not have a dark background.
• We are not big fans of grapes on the label unless extremely stylised. Nor do we like wine glasses, wine bottles.

```html
<!DOCTYPE html>
<html lang="en">
<head>
<meta charset="UTF-8">
<title>Dorvane Vineyards Cabernet Sauvignon Label</title>
<link rel="stylesheet" href="https://fonts.googleapis.com/css2?family=Open+Sans:wght@400;600;700&family=Italianno&display=swap">
<style>
  :root {
    --backdrop: #4b4644;
    --paper: #e9e1d8;
    --paper-shade: #ddd3c8;
    --gold: #b77a45;
    --bronze: #7a4a2c;
    --ink: #6b5546;
    --grape-dark: #2f3552;
    --grape-light: #6f7696;
  }
  html, body {
    margin: 0;
    padding: 0;
    width: 875px;
    height: 1200px;
    overflow: hidden;
    background: var(--backdrop);
  }
  .label {
    position: absolute;
    left: 78px;
    top: 216px;
    width: 720px;
    height: 768px;
    background: radial-gradient(ellipse at center, var(--paper) 55%, var(--paper-shade) 100%);
    box-shadow: 0 2px 8px rgba(0,0,0,0.25);
  }
  .label-frame {
    position: absolute;
    inset: 0;
  }
  .crest {
    position: absolute;
    top: 96px;
    left: 0;
    width: 100%;
    display: flex;
    justify-content: center;
    align-items: center;
    gap: 6px;
  }
  .crest-rule {
    width: 58px;
    height: 2px;
    background: var(--bronze);
  }
  .crest-mark {
    width: 22px;
    height: 22px;
    border-radius: 50%;
    background: var(--gold);
    opacity: 0.75;
  }
  .brand {
    position: absolute;
    top: 150px;
    left: 0;
    width: 100%;
    text-align: center;
    font-family: "Open Sans", sans-serif;
    font-weight: 600;
    font-size: 15px;
    letter-spacing: 4px;
    text-transform: uppercase;
    color: var(--ink);
  }
  .varietal {
    position: absolute;
    top: 204px;
    left: 0;
    width: 100%;
    margin: 0;
    text-align: center;
    font-family: "Open Sans", sans-serif;
    font-weight: 700;
    font-size: 30px;
    line-height: 40px;
    letter-spacing: 1.5px;
    text-transform: uppercase;
    color: var(--bronze);
  }
  .wine-type {
    position: absolute;
    top: 247px;
    left: 0;
    width: 100%;
    text-align: center;
    font-family: "Open Sans", sans-serif;
    font-size: 16px;
    line-height: 22px;
    letter-spacing: 0.5px;
    color: var(--ink);
  }
  .grape-art {
    position: absolute;
    left: 280px;
    top: 330px;
    width: 156px;
    height: 160px;
    border-radius: 45% 45% 50% 50% / 35% 35% 65% 65%;
    background: radial-gradient(circle at 45% 40%, var(--grape-light), var(--grape-dark));
  }
  .tagline {
    position: absolute;
    top: 520px;
    left: 0;
    width: 100%;
    text-align: center;
    font-family: "Italianno", cursive;
    font-size: 58px;
    line-height: 70px;
    word-spacing: 14px;
    color: var(--gold);
  }
  .vintage {
    position: absolute;
    top: 648px;
    left: 0;
    width: 100%;
    text-align: center;
    font-family: "Open Sans", sans-serif;
    font-size: 26px;
    line-height: 34px;
    color: var(--ink);
  }
</style>
</head>
<body>
  <div class="label">
    <svg class="label-frame" width="720" height="768" viewBox="0 0 720 768" aria-hidden="true">
      <defs>
        <linearGradient id="gold-foil" x1="0" y1="0" x2="1" y2="1">
          <stop offset="0" stop-color="#c98a52"/>
          <stop offset="0.5" stop-color="#e8b584"/>
          <stop offset="1" stop-color="#a8683a"/>
        </linearGradient>
      </defs>
      <polygon points="72,44 648,44 678,74 678,694 648,724 72,724 42,694 42,74"
               fill="none" stroke="url(#gold-foil)" stroke-width="5"/>
      <polygon points="80,56 640,56 666,82 666,686 640,712 80,712 54,686 54,82"
               fill="none" stroke="url(#gold-foil)" stroke-width="2"/>
    </svg>

    <div class="crest">
      <span class="crest-rule"></span>
      <span class="crest-mark" role="img" aria-label="Small gold ornament"></span>
      <span class="crest-rule"></span>
    </div>

    <div class="brand">Dorvane Vineyards</div>
    <h1 class="varietal">Cabernet Sauvignon</h1>
    <div class="wine-type">RED WINE</div>

    <div class="grape-art" role="img" aria-label="Illustration of a bunch of dark blue grapes on a stem"></div>

    <div class="tagline">Premium Wine</div>
    <div class="vintage">·2014·</div>
  </div>
</body>
</html>
```